Tidy Tuition Brochure

We offer payment processing and customer service solutions for the parents of Charter schools in the United States.
(More info: http://en.refvaultia.org/wiki/Charter_schools_in_the_United_States )

We have some content and are looking to make an 11x17 back and front design collateral piece. We are also looking for business cards and a 10'x10' trade show booth - separate projects but we can probably use the same designer across both.

Target Market(s)

School Administrators, people who work in school offices, specifically people who work with quickbooks or accounting software for schools.

Industry/Entity Type

Trade

Colors

Designer to choose colors to be used in the design.

Requirements
Must have
• Must have 2-4 pages, maybe 8 pages 1/2 size. It must use most of the content I included.
Nice to have
• I would like photos included - but realize that may not be possible given the space requirement.
Should not have
• Too many fonts, anything that is too glitzy.

```html
<!DOCTYPE html>
<html lang="en">
<head>
<meta charset="utf-8">
<title>Tidy Tuition – Payment Options</title>
<link href="https://fonts.googleapis.com/css2?family=Raleway:wght@300;400;600;700&display=swap" rel="stylesheet">
<style>
  :root {
    --brand-blue: #1b6fae;
    --brand-blue-text: #2677bd;
    --panel-pale: #eaf5fc;
    --badge-navy: #1d4d91;
    --badge-soft: #3a68a8;
    --white: #ffffff;
    --photo-light: #e9eef2;
    --photo-warm: #d8d2c8;
  }
  * { box-sizing: border-box; margin: 0; padding: 0; }
  html, body { width: 1200px; height: 776px; overflow: hidden; background: var(--white); }
  body { font-family: "Raleway", "Helvetica Neue", Arial, sans-serif; }
  .spread { position: relative; width: 1200px; height: 776px; }

  .methods-panel {
    position: absolute; left: 0; top: 0; width: 600px; height: 420px;
    background: var(--brand-blue);
  }
  .types-panel {
    position: absolute; left: 600px; top: 0; width: 600px; height: 420px;
    background: var(--panel-pale);
  }
  .section-title {
    position: absolute; top: 39px;
    font-weight: 400; line-height: 1; white-space: nowrap;
  }
  .methods-panel .section-title { left: 27px; color: var(--white); font-size: 35px; letter-spacing: 0.3px; }
  .types-panel .section-title { left: 22px; color: var(--brand-blue-text); font-size: 33px; letter-spacing: 0.2px; }

  .method-grid {
    position: absolute; left: 54px; top: 127px;
    display: grid; grid-template-columns: 199px 199px; column-gap: 78px; row-gap: 22px;
    list-style: none;
  }
  .method {
    height: 32px; background: var(--white); color: var(--brand-blue-text);
    display: flex; align-items: center; justify-content: center;
    font-size: 16.2px; font-weight: 400; white-space: nowrap;
  }

  .payment-types {
    position: absolute; left: 22px; top: 96px; list-style: none;
    color: var(--brand-blue-text); font-size: 14.2px; line-height: 16.5px; font-weight: 400;
    white-space: nowrap;
  }
  .payment-types li::before { content: "- "; }

  .card-badge {
    position: absolute; left: 1041px; top: 391px; width: 133px; height: 125px;
    background: var(--badge-navy); border-radius: 4px;
    display: flex; flex-direction: column; align-items: center; justify-content: flex-end;
    padding-bottom: 6px;
  }
  .card-badge-art {
    width: 100px; height: 88px; margin-bottom: 8px; border-radius: 3px;
    background: linear-gradient(160deg, var(--badge-soft), var(--badge-navy));
  }
  .card-badge-label { color: var(--white); font-size: 10px; font-weight: 700; letter-spacing: 0.2px; }

  .photo { position: absolute; top: 420px; height: 356px; }
  .photo-office {
    left: 0; width: 600px;
    background: linear-gradient(100deg, var(--photo-light) 0%, #f6f8fa 45%, #cfdbe6 70%, #2d5e9c 85%, #e8edf1 100%);
  }
  .photo-study {
    left: 602px; width: 598px;
    background: linear-gradient(90deg, var(--photo-warm) 0%, #f2f2f0 30%, #6f8fb8 60%, #eef0f1 85%, #d9d6d0 100%);
  }
</style>
</head>
<body>
<main class="spread">
  <section class="methods-panel">
    <h2 class="section-title">HOW CAN THEY PAY?</h2>
    <ul class="method-grid">
      <li class="method">Invoices</li>
      <li class="method">Mobile Payments</li>
      <li class="method">E-Invoices</li>
      <li class="method">Automatic Bank Transfers</li>
      <li class="method">Shopping Cart</li>
      <li class="method">Credit Card Payments</li>
      <li class="method">Donation Handling</li>
      <li class="method">Phone Payments</li>
      <li class="method">In-Person Payments</li>
      <li class="method">Mailed Payments</li>
    </ul>
  </section>

  <section class="types-panel">
    <h2 class="section-title">WHAT TYPES OF PAYMENTS:</h2>
    <ul class="payment-types">
      <li>Payments for Damages/Repairs</li>
      <li>Payments for Goods/Services</li>
      <li>Payments for Extracurricular/Non-Curricular Activities</li>
      <li>Payments for Activities that Supplement a Class/Educational Program</li>
      <li>Payments for Uniforms/ Personal Athletic Equipment</li>
      <li>Payments for Registration / Security Deposits</li>
      <li>Payments for Extended Care Hours / Late Pickups</li>
      <li>Payments for Supplemental Field Trips</li>
      <li>Payments for Voluntary Student Insurance</li>
      <li>Payments for Technology Equipment / Musical Instruments</li>
      <li>Payments for Lab and Shop Classes</li>
      <li>Payments for Student Publications</li>
      <li>Payments for Graduation Announcements</li>
      <li>Payments for Class Rings</li>
      <li>Payments for Post-Secondary Instructional Programs</li>
      <li>Payments for Lost and Destroyed Textbooks/Workbooks/Library Books</li>
      <li>Payments for Voluntary Student Insurance</li>
      <li>Payments for Donations / Gifts</li>
    </ul>
  </section>

  <div class="photo photo-office" role="img" aria-label="Photo: woman in a blue shirt holding a tablet at a bright office table, a colleague working on a laptop behind her"></div>
  <div class="photo photo-study" role="img" aria-label="Photo: man in a checked shirt reviewing a clipboard at a laptop in front of a bookshelf"></div>

  <aside class="card-badge">
    <div class="card-badge-art" role="img" aria-label="Illustration: paying by card with a phone and card reader"></div>
    <span class="card-badge-label">CARD PAYMENT</span>
  </aside>
</main>
</body>
</html>
```